Clean and modern business cards

Looking for an updated business card design for my dental office “corvanta dental” . Looking for a modern clean / sleek design . I’m thinking black background but open to seeing other options . One side needs to have an appointment card . Card needs to have logo, dentist name , phone, email , address . I’ve attached couple of cards I thought were cool as well as my logo
Target Market(s)
Dental patients
Industry/Entity Type
Dentistry
Contact Information for Business Card
Phone email address

```html
<!DOCTYPE html>
<html lang="en">
<head>
<meta charset="utf-8">
<title>Corvanta Dental – Business Card</title>
<link rel="stylesheet" href="https://fonts.googleapis.com/css2?family=Roboto:wght@400;500;700&family=Noto+Sans:wght@400;600&display=swap">
<style>
  :root {
    --backdrop: #7a7a7a;
    --card-dark: #141414;
    --card-light: #ffffff;
    --card-edge: #bdbdbd;
    --text-light: #f2f2f2;
    --text-dark: #1e1e1e;
    --accent: #1aa3d4;
    --decor: #d9d9d9;
  }
  * { box-sizing: border-box; margin: 0; padding: 0; }
  html, body { width: 1200px; height: 1200px; overflow: hidden; }
  body { background: var(--backdrop); position: relative; font-family: "Roboto", Arial, sans-serif; }

  .card {
    position: absolute;
    left: 228px;
    width: 744px;
    height: 426px;
    border-radius: 38px;
    overflow: hidden;
  }
  .card--front { top: 144px; background: var(--card-dark); color: var(--text-light); }
  .card--back { top: 666px; background: var(--card-light); border: 2px solid var(--card-edge); color: var(--text-dark); font-family: "Noto Sans", Arial, sans-serif; }

  /* Front */
  .brand { position: absolute; left: 28px; top: 28px; display: flex; align-items: center; gap: 26px; }
  .brand__dot { width: 130px; height: 130px; border-radius: 50%; background: var(--accent); }
  .brand__name { font-family: "Roboto", Arial, sans-serif; font-weight: 500; color: var(--text-light); line-height: 1; }
  .brand__name-main { display: block; font-size: 52px; letter-spacing: 1px; }
  .brand__name-sub { display: block; font-size: 25px; letter-spacing: 5px; margin-top: 8px; text-align: right; }

  .dentist { position: absolute; left: 34px; top: 236px; display: flex; align-items: center; gap: 16px; }
  .dentist__bar { width: 7px; height: 28px; background: var(--accent); }
  .dentist__name { font-size: 25px; font-weight: 700; }

  .contact { position: absolute; left: 26px; top: 284px; list-style: none; }
  .contact__item { display: flex; align-items: center; gap: 10px; height: 29px; font-size: 20px; }
  .contact__icon { width: 22px; height: 22px; flex: none; }

  /* Back */
  .decor-mark {
    position: absolute; left: 0; top: 30px; width: 235px; height: 370px;
    border-radius: 0 120px 120px 0;
    background: radial-gradient(ellipse at 35% 45%, var(--decor) 0%, var(--decor) 45%, rgba(217,217,217,0) 78%);
  }
  .appointment { position: absolute; left: 281px; top: 84px; width: 360px; }
  .appointment__title { font-size: 22px; font-weight: 600; margin-bottom: 34px; }
  .appointment__field { display: flex; align-items: flex-end; font-size: 20px; height: 30px; margin-bottom: 28px; }
  .appointment__label { width: 57px; }
  .appointment__line { flex: 1; border-bottom: 1.5px solid var(--text-dark); height: 22px; }
  .appointment__note { font-size: 17.5px; line-height: 25px; margin-top: 8px; }
</style>
</head>
<body>
  <section class="card card--front">
    <div class="brand">
      <span class="brand__dot"></span>
      <div class="brand__name">
        <span class="brand__name-main">CORVANTA</span>
        <span class="brand__name-sub">DENTAL</span>
      </div>
    </div>

    <div class="dentist">
      <span class="dentist__bar"></span>
      <span class="dentist__name">Dr. Elan Varkov</span>
    </div>

    <ul class="contact">
      <li class="contact__item">
        <svg class="contact__icon" viewBox="0 0 24 24" fill="none" stroke="var(--accent)" stroke-width="1.5"><circle cx="12" cy="12" r="10"/><path d="M9 7c-1 1-1 3 1 6s4 4 5 4l1-2-2-1-1 1c-1-.5-2.5-2-3-3l1-1-1-2z"/></svg>
        <span>204.555.0172</span>
      </li>
      <li class="contact__item">
        <svg class="contact__icon" viewBox="0 0 24 24" fill="none" stroke="var(--accent)" stroke-width="1.5"><rect x="3" y="6" width="18" height="12"/><path d="M3 6l9 7 9-7"/></svg>
        <span>contact@corvantawpg.ca</span>
      </li>
      <li class="contact__item">
        <svg class="contact__icon" viewBox="0 0 24 24" fill="none" stroke="var(--accent)" stroke-width="1.5"><circle cx="12" cy="12" r="9"/><ellipse cx="12" cy="12" rx="4" ry="9"/><path d="M3 12h18M5 7h14M5 17h14"/></svg>
        <span>www.corvantawpg.ca</span>
      </li>
      <li class="contact__item">
        <svg class="contact__icon" viewBox="0 0 24 24" fill="var(--accent)"><path d="M12 2a7 7 0 0 0-7 7c0 5 7 13 7 13s7-8 7-13a7 7 0 0 0-7-7zm0 10a3 3 0 1 1 0-6 3 3 0 0 1 0 6z"/></svg>
        <span>2140 Larchmont Ave, Winnipeg, MB</span>
      </li>
    </ul>
  </section>

  <section class="card card--back">
    <div class="decor-mark" role="img" aria-label="Faint grey brand symbol decoration"></div>
    <div class="appointment">
      <h2 class="appointment__title">Your Next Appoinment is on:</h2>
      <div class="appointment__field"><span class="appointment__label">Date</span><span class="appointment__line"></span></div>
      <div class="appointment__field"><span class="appointment__label">Time</span><span class="appointment__line"></span></div>
      <p class="appointment__note">To cancel or reschedule, please notify us at least 48 hours prior to your scheduled appointment.</p>
    </div>
  </section>
</body>
</html>
```